Stationary for wedding and portrait photographer
4x6 Gift Voucher, Business Card, Letterhead, 5x7 folding card
Stationary for wedding and portrait photographer - Photography
Creative Brief
Simple
Martha Quill
Wedding and Portrait Photography
Located in Alder County, PA. Available worldwide for travel.
martha@martha-quill.com
www.martha-quill.com
In addition to the business card I need a 4x6 gift voucher designed. The text for the gift voucher needs to include: A gift from Martha Quill This gift voucher entitles the bearer____________ to a double makeover & photo shoot with Martha Quill plus $100 towards portraits. Total value $275. It's the ultimate girl's day out. Celebrate your relationships. Enjoy this beautiful session with your mom, daughter, or best friend. Remember to book a night out afterwards, because you will look beautiful! This voucher expires _________. Disclaimer: This voucher is not redeemable for cash & we can not be held responsible for how beautiful you will look. The 5x7 folding card just needs the front designed, inside is blank.
MarthaQuill MarthaQuill
I prefer square corners over rounded.
Material should match my website www.martha-quill.com
I actually need the business card to be double sided.

```html
<!DOCTYPE html>
<html lang="en">
<head>
<meta charset="utf-8">
<title>Martha Quill Stationery</title>
<link rel="stylesheet" href="https://fonts.googleapis.com/css2?family=Lato:wght@300;400;700&display=swap">
<style>
  :root {
    --backdrop: #e6e8ea;
    --paper: #ffffff;
    --aqua: #bfe2e5;
    --aqua-deep: #8fc7cc;
    --slate: #85898d;
    --ink: #5d6164;
    --ink-soft: #9a9ea1;
    --shadow: rgba(40, 50, 60, 0.18);
  }
  * { box-sizing: border-box; margin: 0; padding: 0; }
  html, body { width: 1200px; height: 547px; overflow: hidden; }
  body {
    background: var(--backdrop);
    font-family: "Lato", sans-serif;
    color: var(--ink);
    position: relative;
  }
  .piece {
    position: absolute;
    box-shadow: 0 3px 10px var(--shadow);
  }
  .wordmark {
    font-family: "Lato", sans-serif;
    font-weight: 300;
    letter-spacing: 0.5px;
  }

  /* Business cards */
  .business-card { width: 175px; height: 100px; display: flex; flex-direction: column; justify-content: center; align-items: center; }
  .business-card--front { left: 34px; top: 150px; background: var(--slate); color: var(--paper); }
  .business-card--front .wordmark { font-size: 20px; }
  .business-card--back { left: 34px; top: 268px; background: var(--aqua); color: var(--ink); font-size: 7.5px; line-height: 1.6; text-align: center; }
  .business-card--back .wordmark { font-size: 13px; margin-bottom: 4px; }
  .business-card--photo { left: 470px; top: 378px; width: 210px; height: 120px; background: var(--paper); flex-direction: row; justify-content: flex-start; gap: 12px; padding: 14px; border-bottom: 8px solid var(--aqua); }
  .business-card--photo .photo { width: 70px; height: 80px; background: linear-gradient(160deg, #e9d8cf, #c9a89a); flex: none; }
  .business-card--photo .details { font-size: 7px; line-height: 1.7; }
  .business-card--photo .wordmark { font-size: 13px; color: var(--aqua-deep); margin-bottom: 4px; }

  /* Letterhead */
  .letterhead { left: 228px; top: 34px; width: 222px; height: 314px; background: var(--paper); padding: 22px 22px 14px; display: flex; flex-direction: column; }
  .letterhead__mark { text-align: center; font-size: 16px; color: var(--aqua-deep); margin-bottom: 22px; }
  .letterhead__body { font-size: 6.5px; line-height: 1.7; color: var(--ink); flex: 1; }
  .letterhead__body p { margin-bottom: 7px; }
  .letterhead__signature { font-size: 9px; color: var(--aqua-deep); }
  .letterhead__footer { border-top: 1px solid var(--aqua); padding-top: 6px; font-size: 6px; text-align: center; color: var(--ink-soft); letter-spacing: 0.4px; }

  /* Envelope */
  .envelope { left: 470px; top: 120px; width: 290px; height: 230px; box-shadow: none; }
  .envelope svg { position: absolute; left: 0; top: 0; filter: drop-shadow(0 3px 6px var(--shadow)); }
  .envelope__mark { position: absolute; left: 14px; top: 92px; font-size: 11px; color: var(--aqua-deep); }
  .envelope__address { position: absolute; left: 120px; top: 160px; font-size: 8px; line-height: 1.6; color: var(--ink); }

  /* Folding card */
  .folding-card { left: 800px; top: 28px; width: 350px; height: 250px; background: var(--aqua); display: flex; align-items: center; justify-content: center; }
  .folding-card .wordmark { font-size: 34px; color: var(--paper); }

  /* Voucher */
  .voucher { left: 800px; top: 296px; width: 330px; height: 220px; background: var(--paper); padding: 16px 20px; font-size: 7px; line-height: 1.55; }
  .voucher__title { font-size: 14px; font-weight: 300; color: var(--ink); margin-bottom: 8px; }
  .voucher__title .wordmark { color: var(--aqua-deep); }
  .voucher__lead { margin-bottom: 6px; }
  .voucher__total { text-align: right; color: var(--aqua-deep); font-size: 8px; margin-bottom: 6px; }
  .voucher__headline { color: var(--aqua-deep); font-size: 9px; margin-bottom: 3px; }
  .voucher__expiry { margin-top: 6px; }
  .voucher__disclaimer { margin-top: 6px; font-size: 5.5px; color: var(--ink-soft); width: 220px; }
  .voucher__mark { position: absolute; right: 18px; bottom: 14px; font-size: 11px; color: var(--aqua-deep); }

  .caption { position: absolute; font-size: 8px; letter-spacing: 1px; text-transform: uppercase; color: var(--ink-soft); }
  .caption--folding { left: 1004px; top: 282px; }
  .caption--voucher { left: 1136px; top: 506px; }
</style>
</head>
<body>

  <section class="piece business-card business-card--front">
    <span class="wordmark">MarthaQuill</span>
  </section>

  <section class="piece business-card business-card--back">
    <span class="wordmark">MarthaQuill</span>
    <span>Wedding and Portrait Photography</span>
    <span>martha@martha-quill.com</span>
    <span>www.martha-quill.com</span>
  </section>

  <section class="piece letterhead">
    <div class="letterhead__mark wordmark">MarthaQuill</div>
    <div class="letterhead__body">
      <p>Dear Eleanor,</p>
      <p>Thank you for choosing us to capture your wedding day. Your gallery is ready, and every frame holds a quiet joy we hope you will treasure for years to come.</p>
      <p>Warm regards,</p>
      <p class="letterhead__signature">Martha Quill</p>
    </div>
    <div class="letterhead__footer">martha@martha-quill.com &nbsp;|&nbsp; www.martha-quill.com</div>
  </section>

  <section class="piece envelope">
    <svg width="290" height="230" viewBox="0 0 290 230" aria-hidden="true">
      <polygon points="0,80 145,0 290,80" fill="#bfe2e5"/>
      <rect x="0" y="80" width="290" height="150" fill="#ffffff"/>
      <polyline points="0,80 145,150 290,80" fill="none" stroke="#e2eced" stroke-width="1"/>
    </svg>
    <span class="envelope__mark wordmark">MarthaQuill</span>
    <div class="envelope__address">Eleanor Hart<br>12 Linden Lane<br>Westbrook</div>
  </section>

  <section class="piece business-card business-card--photo">
    <div class="photo" role="img" aria-label="Portrait photograph of a bride"></div>
    <div class="details">
      <div class="wordmark">MarthaQuill</div>
      Wedding and Portrait Photography<br>
      Alder County, PA<br>
      martha@martha-quill.com<br>
      www.martha-quill.com
    </div>
  </section>

  <section class="piece folding-card">
    <span class="wordmark">MarthaQuill</span>
  </section>
  <span class="caption caption--folding">5x7 folding card front</span>

  <section class="piece voucher">
    <div class="voucher__title">A gift from <span class="wordmark">MarthaQuill</span></div>
    <p class="voucher__lead">This gift voucher entitles the bearer ____________ to a double makeover &amp; photo shoot with Martha Quill plus $100 towards portraits.</p>
    <p class="voucher__total">Total value $275</p>
    <p class="voucher__headline">It's the ultimate girl's day out.</p>
    <p>Celebrate your relationships. Enjoy this beautiful session with your mom, daughter, or best friend. Remember to book a night out afterwards, because you will look beautiful!</p>
    <p class="voucher__expiry">This voucher expires _________.</p>
    <p class="voucher__disclaimer">Disclaimer: This voucher is not redeemable for cash &amp; we can not be held responsible for how beautiful you will look.</p>
    <span class="voucher__mark wordmark">MarthaQuill</span>
  </section>
  <span class="caption caption--voucher">voucher</span>

</body>
</html>
```